Premium stylish simple clever card design for high end construction company.

I need a business card designed that is a standard size and shape (square edges) that is black in colour, with black edges. All text is to be either grey/silver or yellow/gold. On the front I want the logo (supplied as attachment g5) to be embossed or raised to give a texture. I also want the name of my company "The Kestrel Vault (larger font) construction co. (smaller font)" I like the clean style (found in attachment 56419286) of the black background with silver text. But the triangle is to be gold/yellow.

On the back needs to have my contact details. In silver or gold text.

Liam Porter - Builder
Liam@thekestrelvault.com.au
www.thekestrelvault.com.au
0427391065
Lic 517904k
PO BOX 739 Marlowe Bay NSW 2108

Must look simple, elegant and precise.

My work is of the utmost quality and my business card needs to project that. It needs to be simple and precise. It should scream luxury and confidence. Feel free to get creative with the font and font size. If you google "The Kestrel Vault" you will see it has links to great architecture, art, nature and the fibonacci sequence so i am open to using these ideas also.

Target Market(s)

High End home owners. 30-70 year olds.

Industry/Entity Type

Residential Construction

Contact Information for Business Card

Logo and company name on front. Contact details on back.

Font styles to use
Serif
Sans Serif

Colors
ffcf3e

Requirements
Must have
• black background
Nice to have
• debossed logo (silver and gold)
• debased company name (silver)
Should not have
• It should not look like a standard construction business card with pictures of hammers or tools etc.

```html
<!DOCTYPE html>
<html lang="en">
<head>
<meta charset="utf-8">
<title>The Kestrel Vault – Business Card</title>
<link rel="stylesheet" href="https://fonts.googleapis.com/css2?family=Questrial&display=swap">
<style>
  :root {
    --backdrop: #141414;
    --card: #1c1c1c;
    --card-edge: #0a0a0a;
    --silver: #cfcfcf;
    --silver-soft: #a9a9a9;
    --gold: #ffcf3e;
  }
  * { margin: 0; padding: 0; box-sizing: border-box; }
  html, body {
    width: 1200px;
    height: 1000px;
    overflow: hidden;
    background: var(--backdrop);
    font-family: "Questrial", "Century Gothic", sans-serif;
  }
  .canvas {
    position: relative;
    width: 1200px;
    height: 1000px;
  }
  .card {
    position: absolute;
    top: 357px;
    width: 500px;
    height: 286px;
    background: var(--card);
    border: 1px solid var(--card-edge);
    box-shadow: 0 18px 40px rgba(0, 0, 0, 0.55);
  }
  .card--front { left: 70px; }
  .card--back { left: 630px; }

  /* Front */
  .brand {
    position: absolute;
    top: 54px;
    left: 0;
    width: 100%;
    display: flex;
    flex-direction: column;
    align-items: center;
  }
  .brand__mark {
    width: 58px;
    height: 58px;
    margin-bottom: 14px;
  }
  .brand__name {
    color: var(--silver);
    font-size: 30px;
    letter-spacing: 0.5px;
    text-transform: uppercase;
    white-space: nowrap;
    padding-bottom: 4px;
    border-bottom: 1px solid var(--silver-soft);
  }
  .brand__tagline {
    margin-top: 4px;
    color: var(--silver-soft);
    font-size: 11px;
    letter-spacing: 1px;
    text-transform: uppercase;
  }
  .website {
    position: absolute;
    bottom: 30px;
    left: 0;
    width: 100%;
    text-align: center;
    color: var(--silver-soft);
    font-size: 11px;
    letter-spacing: 2.4px;
  }

  /* Back */
  .contact {
    position: absolute;
    top: 50px;
    left: 42px;
    color: var(--silver);
  }
  .contact__name {
    color: var(--gold);
    font-size: 22px;
    margin-bottom: 6px;
  }
  .contact__role {
    font-size: 14px;
    margin-bottom: 14px;
  }
  .contact__line {
    font-size: 15px;
    line-height: 1.35;
  }
  .details {
    position: absolute;
    right: 42px;
    bottom: 42px;
    color: var(--silver);
    font-size: 13px;
    line-height: 1.5;
  }
</style>
</head>
<body>
<main class="canvas">
  <section class="card card--front" aria-label="Business card front">
    <div class="brand">
      <svg class="brand__mark" viewBox="0 0 58 58" aria-hidden="true">
        <circle cx="29" cy="29" r="25" fill="none" stroke="#cfcfcf" stroke-width="7"/>
      </svg>
      <div class="brand__name">The Kestrel Vault</div>
      <div class="brand__tagline">Construction Co.</div>
    </div>
    <div class="website">www.thekestrelvault.com.au</div>
  </section>

  <section class="card card--back" aria-label="Business card back">
    <div class="contact">
      <div class="contact__name">Liam Porter</div>
      <div class="contact__role">Builder</div>
      <div class="contact__line">Liam@thekestrelvault.com.au</div>
      <div class="contact__line">0427 391 065</div>
    </div>
    <div class="details">
      <div>Lic 517904k</div>
      <div>PO BOX 739 Marlowe Bay</div>
      <div>NSW 2108</div>
    </div>
  </section>
</main>
</body>
</html>
```